Roofing Company Now Hiring and Call Now Facebook Ads

Trying to hire new sales reps in our Alabama market to add to our growing team. This is a great opportunity for any one looking for a career change or looking to add time back to the time they get to spend at home with their families. This is a chance to build a career in one of the fastest growing industries in the country and build financial freedom and a solid future for your family while easily making 6 figures yearly. Sales reps get to set their own schedule, take vacations when they want, and could even choose if they wanted to work in the summer or the winter seasons if they dont like the heat/cold environment. Sales reps are commission based with bonus/incentives for completing task and assignments weekly.

"Let's Talk About Your Roof!" Schedule a free Roof Inspection today!

Needing facebook ads for hiring and a few ads templates for daily post regarding roof inspections and roof replacements, if they are editable it would be easier for me to manage a few templates. This project needs to have a swag/cleanish look that attracts the younger group of people but still make the older group of customer think, man these guys have some solid looking things going on and looks like a well managed and built company. We also target the upper scale areas when seeking customers.

Lets see what yall got! lets Gooo!

Target Market(s)

Property owners, sales reps, homeowners, property managers, job seekers

Industry/Entity Type

Roofing Contractor Storm Restoration Contractor, Construction Contractor

Font styles to use
Sans Serif

Colors
EB3D1F
EC4F4E
F09395
F8D3D4
FCEDEE

Requirements
Must have
• Clean modern professional look with visible red and black colors, we like white too.
Nice to have
• red, black, white, popping eye catching colors.
Should not have
• wrong color red, red is more of a calder ridge otters red, please stay away from the pinkish red.

```html
<!DOCTYPE html>
<html lang="en">
<head>
<meta charset="utf-8">
<title>Crestline Roofing – We Are Hiring</title>
<link rel="stylesheet" href="https://fonts.googleapis.com/css2?family=Anton&family=Poppins:wght@400;500;700;800&display=swap">
<style>
  :root {
    --red: #e31b44;
    --red-deep: #6e0f1f;
    --ink: #000000;
    --white: #ffffff;
    --footer-text: #333333;
    --muted: #555555;
  }
  * { margin: 0; padding: 0; box-sizing: border-box; }
  html, body { width: 1200px; height: 1200px; overflow: hidden; background: var(--white); }
  .poster {
    position: relative;
    width: 1200px;
    height: 1200px;
    background: var(--ink);
    font-family: "Poppins", sans-serif;
    color: var(--white);
    overflow: hidden;
  }
  .backdrop { position: absolute; inset: 0; }
  .brand {
    position: absolute;
    left: 74px; top: 82px;
    display: flex; align-items: center; gap: 14px;
    font-weight: 800; font-size: 40px; letter-spacing: 0.5px; line-height: 1;
  }
  .brand-mark { width: 16px; height: 16px; background: var(--red); }
  .headline-top {
    position: absolute;
    left: 228px; top: 212px;
    font-weight: 800; font-size: 92px; line-height: 1; letter-spacing: 1px;
  }
  .headline-main { position: absolute; left: 0; top: 0; }
  .team-tag {
    position: absolute;
    left: 428px; top: 679px;
    width: 344px; height: 100px;
  }
  .team-tag span {
    position: absolute; left: 0; top: 0; width: 344px; height: 74px;
    display: flex; align-items: center; justify-content: center;
    font-weight: 700; font-size: 33px; letter-spacing: 0.3px;
  }
  .role {
    position: absolute;
    left: 198px; top: 818px;
    display: flex; align-items: center; gap: 28px;
    font-size: 64px; line-height: 1;
  }
  .role-title strong { font-weight: 700; }
  .role-title { font-weight: 400; }
  .location {
    position: absolute;
    left: 435px; top: 926px;
    width: 340px; height: 79px;
    border: 3px solid var(--white);
    border-radius: 14px;
    display: flex; align-items: center;
  }
  .location-icon {
    width: 84px; height: 100%;
    border-right: 3px solid var(--white);
    border-radius: 12px;
    display: flex; align-items: center; justify-content: center;
  }
  .location-name { padding-left: 34px; font-size: 40px; font-weight: 400; }
  .footer {
    position: absolute;
    left: 0; top: 1050px; width: 1200px; height: 150px;
    background: var(--white);
  }
  .footer-rule {
    position: absolute; left: 0; top: 0; width: 100%; height: 7px;
    background: linear-gradient(90deg, var(--red) 0%, var(--red) 35%, var(--red-deep) 75%, #2a0a10 100%);
  }
  .submit-button {
    position: absolute;
    left: 54px; top: 50px;
    width: 228px; height: 58px;
    border-radius: 29px;
    background: linear-gradient(90deg, var(--red) 0%, #8a1025 60%, #1a0508 100%);
    display: flex; align-items: center; justify-content: center;
    font-weight: 800; font-size: 29px; color: var(--white);
  }
  .apply {
    position: absolute;
    right: 137px; top: 46px;
    text-align: right;
  }
  .apply-label { font-size: 17px; color: var(--muted); font-weight: 400; line-height: 1.2; }
  .apply-email { font-size: 28px; font-weight: 700; color: var(--footer-text); line-height: 1.2; }
  .apply-icon { position: absolute; left: 1080px; top: 55px; }
</style>
</head>
<body>
<main class="poster">
  <svg class="backdrop" width="1200" height="1200" viewBox="0 0 1200 1200" aria-hidden="true">
    <defs>
      <linearGradient id="orbFade" x1="0" y1="0" x2="1" y2="0">
        <stop offset="0" stop-color="#e31b44"/>
        <stop offset="1" stop-color="#1a0408"/>
      </linearGradient>
      <linearGradient id="ringFade" x1="0" y1="0" x2="1" y2="0">
        <stop offset="0" stop-color="#e31b44"/>
        <stop offset="1" stop-color="#4a0a14"/>
      </linearGradient>
    </defs>
    <circle cx="245" cy="483" r="107" fill="url(#orbFade)"/>
    <circle cx="845" cy="418" r="215" fill="url(#orbFade)"/>
    <path d="M665 232 A279 279 0 1 1 665 587" fill="none" stroke="url(#ringFade)" stroke-width="3"/>
    <circle cx="665" cy="232" r="12" fill="#e31b44"/>
    <circle cx="665" cy="587" r="12" fill="#e31b44"/>
    <g class="dot-grid" fill="#e31b44">
      <circle cx="1057" cy="78" r="2.6"/><circle cx="1069" cy="78" r="2.6"/><circle cx="1081" cy="78" r="2.6"/><circle cx="1093" cy="78" r="2.6"/><circle cx="1105" cy="78" r="2.6"/><circle cx="1117" cy="78" r="2.6"/>
      <circle cx="1057" cy="97" r="2.6"/><circle cx="1069" cy="97" r="2.6"/><circle cx="1081" cy="97" r="2.6"/><circle cx="1093" cy="97" r="2.6"/><circle cx="1105" cy="97" r="2.6"/><circle cx="1117" cy="97" r="2.6"/>
      <circle cx="1057" cy="116" r="2.6"/><circle cx="1069" cy="116" r="2.6"/><circle cx="1081" cy="116" r="2.6"/><circle cx="1093" cy="116" r="2.6"/><circle cx="1105" cy="116" r="2.6"/><circle cx="1117" cy="116" r="2.6"/>
    </g>
  </svg>

  <div class="brand"><span class="brand-mark"></span>CRESTLINE ROOFING</div>

  <h1 class="headline-top">WE ARE</h1>
  <svg class="headline-main" width="1200" height="1200" viewBox="0 0 1200 1200" role="img" aria-label="Hiring!">
    <text x="225" y="505" textLength="755" lengthAdjust="spacingAndGlyphs"
          font-family="Anton, sans-serif" font-size="216" fill="none"
          stroke="#ffffff" stroke-width="3.5" stroke-linejoin="miter">HIRING!</text>
  </svg>

  <div class="team-tag">
    <svg width="344" height="100" viewBox="0 0 344 100" aria-hidden="true">
      <path d="M10 1.5 H334 A8.5 8.5 0 0 1 342.5 10 V64 A8.5 8.5 0 0 1 334 72.5 H214 L198 97 L125 72.5 H10 A8.5 8.5 0 0 1 1.5 64 V10 A8.5 8.5 0 0 1 10 1.5 Z"
            fill="none" stroke="#e31b44" stroke-width="3" stroke-linejoin="round"/>
    </svg>
    <span>JOIN OUR TEAM</span>
  </div>

  <div class="role">
    <svg width="72" height="52" viewBox="0 0 72 52" aria-hidden="true">
      <path d="M0 0 H18 L38 26 L18 52 H0 L20 26 Z M32 0 H50 L70 26 L50 52 H32 L52 26 Z" fill="#e31b44"/>
    </svg>
    <p class="role-title"><strong>Sales</strong> Representative</p>
  </div>

  <div class="location">
    <div class="location-icon">
      <svg width="44" height="56" viewBox="0 0 44 56" aria-hidden="true">
        <path d="M22 2 C11 2 4 10 4 20 C4 33 22 46 22 46 C22 46 40 33 40 20 C40 10 33 2 22 2 Z" fill="#ffffff"/>
        <circle cx="22" cy="19" r="7" fill="#000000"/>
        <ellipse cx="22" cy="50" rx="17" ry="4.5" fill="none" stroke="#ffffff" stroke-width="3"/>
      </svg>
    </div>
    <span class="location-name">Alabama</span>
  </div>

  <footer class="footer">
    <div class="footer-rule"></div>
    <div class="submit-button">SUBMIT CV</div>
    <div class="apply">
      <p class="apply-label">APPLY HERE</p>
      <p class="apply-email">INFO@CRESTLINEGA.COM</p>
    </div>
    <svg class="apply-icon" width="56" height="42" viewBox="0 0 56 42" aria-hidden="true">
      <rect x="1.5" y="1.5" width="53" height="39" rx="5" fill="none" stroke="#111111" stroke-width="3"/>
      <path d="M4 5 L28 25 L52 5 M4 37 L21 20 M52 37 L35 20" fill="none" stroke="#111111" stroke-width="2.5"/>
    </svg>
  </footer>
</main>
</body>
</html>
```